International Company needs a Letterhead & Envelope Design

Our Company name is Brightfold Harbor Limited.
We'd like to ask the Designers for the luxurious and sophisticated design. Our logo is very simple and neat with letter logos, so we look forward to more professional and refined designs from Designers.
We look forward to providing you with a great design.
Thanks very much in advance.

```html
<!DOCTYPE html>
<html lang="en">
<head>
<meta charset="utf-8">
<title>Brightfold Harbor Limited — Letterhead</title>
<link rel="stylesheet" href="https://fonts.googleapis.com/css2?family=Lato:ital,wght@0,400;0,700;0,900;1,400&display=swap">
<style>
  :root {
    --backdrop: #e4e3e6;
    --paper: #ffffff;
    --ink: #3a3a3c;
    --ink-soft: #5c5c60;
    --ink-dark: #1f1f21;
    --band-dark: #202022;
    --band-mid: #6e6e72;
    --band-light: #c9c9cc;
    --signature-tone: #d9d9dc;
    --band-text: #f2f2f2;
  }
  * { box-sizing: border-box; margin: 0; padding: 0; }
  html, body {
    width: 1200px; height: 800px; overflow: hidden;
    background: var(--backdrop);
    font-family: "Lato", sans-serif;
    color: var(--ink);
  }
  .letterhead {
    position: absolute; left: 330px; top: 18px;
    width: 540px; height: 764px;
    background: var(--paper);
    box-shadow: 0 2px 10px rgba(0,0,0,0.12);
    overflow: hidden;
  }
  .wordmark {
    position: absolute; left: 240px; top: 44px;
    font-weight: 900; font-size: 30px; letter-spacing: 1px;
    color: var(--ink-dark);
  }
  .recipient {
    position: absolute; left: 70px; top: 112px;
    font-size: 8.5px; line-height: 1.35; color: var(--ink-soft);
  }
  .recipient .date { margin-bottom: 6px; }
  .recipient .name { font-weight: 700; color: var(--ink); }
  .letter-body {
    position: absolute; left: 70px; top: 190px; width: 285px;
    font-size: 8.5px; line-height: 1.4; color: var(--ink);
  }
  .letter-body .salutation { margin-bottom: 8px; color: var(--ink-soft); }
  .letter-body p { margin-bottom: 9px; text-align: justify; }
  .closing { margin-top: 14px; font-size: 8.5px; line-height: 1.4; }
  .closing .signature {
    width: 150px; height: 26px; margin: 4px 0;
    background: var(--signature-tone); border-radius: 3px;
  }
  .closing .title { font-weight: 700; }
  .closing .company { color: var(--ink-soft); }
  .sender {
    position: absolute; right: 28px; top: 190px; width: 140px;
    text-align: right; font-size: 8px; line-height: 1.45; color: var(--ink-soft);
    font-style: normal;
  }
  .sender .line { display: flex; justify-content: flex-end; align-items: center; gap: 5px; }
  .sender svg { width: 8px; height: 8px; fill: var(--ink); flex: none; }
  .side-bar {
    position: absolute; right: 0; top: 208px; width: 12px; height: 78px;
    background: linear-gradient(var(--band-mid), var(--band-dark));
  }
  .swoosh { position: absolute; left: 0; top: 470px; width: 110px; height: 294px; }
  .web-address {
    position: absolute; left: 12px; top: 745px;
    transform: rotate(-90deg); transform-origin: left top;
    font-size: 8.5px; line-height: 11px; color: var(--band-text);
    letter-spacing: 0.3px; white-space: nowrap;
  }
</style>
</head>
<body>
  <main class="letterhead">
    <div class="wordmark">BRIGHTFOLD</div>

    <section class="recipient">
      <div class="date">January 1, 2050</div>
      <div class="name">Daniel Ward</div>
      <div>Managing Director</div>
      <div>Co. Street, Building/Suite</div>
      <div>City/State, Zip Code</div>
    </section>

    <section class="letter-body">
      <div class="salutation">Dear Laura Benton,</div>
      <p>Lorem ipsum dolor sit amet, consectetuer adipiscing elit, sed diam nonummy nibh euismod tincidunt ut laoreet dolore magna aliquam erat volutpat. Ut wisi enim ad minim veniam, quis nostrud exerci tation ullamcorper suscipit lobortis nisl ut aliquip ex ea commodo consequat. Duis dolore te feugait nulla facilisi. Nam liber tempor cum soluta nobis eleifend option congue nihil imperdiet doming id quod mazim placerat facer possim assum. Lorem ipsum dolor sit amet, consectetuer adipiscing elit, sed diam nonummy nibh euismod tincidunt ut laoreet dolore magna aliquam erat volutpat. Ut wisi enim ad minim veniam, quis nostrud exerci tation ullamcorper suscipit lobortis nisl ut aliquip ex ea commodo consequat.</p>
      <p>Consectetuer adipiscing elit, sed diam nonummy nibh euismod tincidunt ut laoreet dolore magna aliquam erat volutpat. Ut wisi enim ad minim veniam, quis nostrud exerci tation ullamcorper suscipit lobortis nisl ut aliquip ex ea commodo consequat. Consectetuer adipiscing elit, sed diam nonummy nibh euismod tincidunt ut laoreet dolore magna aliquam erat volutpat. Ut wisi enim ad minim veniam, quis nostrud exerci tation ullamcorper suscipit lobortis nisl ut aliquip ex ea commodo consequat.</p>
      <p>Duis dolore te feugait nulla facilisi. Nam liber tempor cum soluta nobis eleifend option congue nihil imperdiet doming id quod mazim placerat facer possim assum. Duis dolore te feugait nulla facilisi. Nam liber tempor cum soluta nobis eleifend option congue nihil imperdiet doming id quod mazim placerat facer possim assum.</p>
      <div class="closing">
        <div>Sincerely Yours,</div>
        <div class="signature" role="img" aria-label="Handwritten signature of the managing director"></div>
        <div class="title">Authorized Managing Director</div>
        <div class="company">Company Name Here</div>
      </div>
    </section>

    <address class="sender">
      <div>Brightfold Harbor Limited</div>
      <div>Co. Street, Suite, Building</div>
      <div>City/State, Zip Code</div>
      <div class="line">210.555.0140
        <svg viewBox="0 0 10 10"><path d="M2 0.5 L3.6 0.5 L4.4 2.8 L3.3 3.7 Q4.2 5.8 6.3 6.7 L7.2 5.6 L9.5 6.4 L9.5 8 Q9.5 9.5 8 9.5 Q0.5 9 0.5 2 Q0.5 0.5 2 0.5Z"/></svg></div>
      <div class="line">210.555.0190
        <svg viewBox="0 0 10 10"><rect x="1.5" y="0.5" width="7" height="3"/><rect x="0.5" y="4" width="9" height="5.5" rx="1"/></svg></div>
      <div class="line">info@brightfold-harbor.com
        <svg viewBox="0 0 10 10"><path d="M0.5 2 H9.5 V8.5 H0.5Z M0.5 2 L5 5.5 L9.5 2" fill="none" stroke="#3a3a3c" stroke-width="1"/></svg></div>
    </address>

    <div class="side-bar"></div>

    <svg class="swoosh" viewBox="0 0 110 294" preserveAspectRatio="none" aria-hidden="true">
      <defs>
        <linearGradient id="bandShade" x1="0" y1="0" x2="1" y2="0">
          <stop offset="0" stop-color="#202022"/>
          <stop offset="0.7" stop-color="#3a3a3d"/>
          <stop offset="1" stop-color="#7a7a7e"/>
        </linearGradient>
      </defs>
      <path d="M0 0 Q30 10 40 60 Q55 200 110 294 L0 294Z" fill="var(--band-light)"/>
      <path d="M0 8 Q22 18 30 70 Q44 210 96 294 L0 294Z" fill="#ffffff"/>
      <path d="M0 14 Q18 26 24 80 Q36 215 86 294 L0 294Z" fill="url(#bandShade)"/>
    </svg>
    <div class="web-address">www.brightfold-harbor.com</div>
  </main>
</body>
</html>
```